Plate Bright Workshop (workshop to teach people to eat fruits and vegetables)

Double sided DL Flyer

Free Community Workshop
Plate Bright Live Lively
Central Coast NSW

Copy to appear on flyer side one:-
PLATE BRIGHT LIVE LIVELY
interactive workshops
March-April 2019
Presented by qualified nutritionist

Food for healthier happier life for you and your family (free to central coast residents - all ages welcome

Side 2
Learn About:-
Foods that improve your health
basic nutrition
gut brain connection
portion size
menu planning
preparation
eating

Benefits
Improved health
Improved Energy
Manage chronic illness
diabetes type II
cholesterol
Blood Pressure
Family fun

Food Tastings
Lucky Door Prize

Reserve for spot online @ www.platebright.com.au or call 0462 508 731
Supported by Harbourline Shire Council (Logo) Harbourline Rugby Social Club (Logo) Pindara Veterans Club (Logo)

I would like to see a flyer that is bright, fun and fresh with images of fresh food.

Target Market(s)

Women 30 plus

Industry/Entity Type

Health And Wellness

Logo Text

PLATE BRIGHT LIVE LIVELY

Font styles to use
Other font styles liked:
• bold clean

Colors
f37122
9bcb3c
fbed22
ec1f27
e34297

Requirements
Must have
• bright eye catching colours featuring fresh fruit and vegetables
• I have attached a some images of designs I like
Nice to have
• Im happy for the designer to change copy to create a clean flyer without loosing essential information
• I like the feel of the banner on my facebook page
• Kindly Nourish - Plate Bright Live Lively with Megan Troute
• https://www.facebook.com/kindlynourishoz/
Should not have
• old fashioned images

```html
<!DOCTYPE html>
<html lang="en">
<head>
<meta charset="utf-8">
<title>Plate Bright Live Lively – DL Flyer</title>
<link rel="stylesheet" href="https://fonts.googleapis.com/css2?family=Bebas+Neue&family=Montserrat:wght@600;700;900&family=Permanent+Marker&family=Roboto+Condensed:wght@400;700&display=swap">
<style>
  :root{
    --page:#e6e7e9;
    --sky-light:#c9ecfc;
    --sky:#5fbdf0;
    --sky-deep:#1b93dc;
    --ink-blue:#1b9be0;
    --band-blue:#7fc9f1;
    --pink:#e8174f;
    --plum:#4e2743;
    --white:#ffffff;
    --paper:#f6f6f4;
    --tab-grey:#e9ecef;
    --star:#f3e84a;
  }
  *{box-sizing:border-box;margin:0;padding:0}
  html,body{width:1200px;height:1200px;overflow:hidden;background:var(--page)}
  .canvas{position:relative;width:1200px;height:1200px}
  .flyer{position:absolute;top:146px;width:409px;height:866px;overflow:hidden;box-shadow:0 2px 6px rgba(0,0,0,.18)}
  .hand{font-family:"Permanent Marker","Montserrat",sans-serif}

  /* ---------- front ---------- */
  .flyer--front{left:146px;background:radial-gradient(ellipse 75% 45% at 50% 22%,var(--sky-light) 0%,var(--sky) 55%,var(--sky-deep) 100%)}
  .front__fruit-art{position:absolute;left:66px;top:58px;width:264px;height:224px;border-radius:24px;
    background:linear-gradient(160deg,rgba(247,162,58,.55) 0%,rgba(200,60,50,.45) 45%,rgba(242,210,58,.6) 100%)}
  .front__headline{position:absolute;left:0;right:0;top:304px;text-align:center;color:var(--white);line-height:.86}
  .front__headline .heavy{display:block;font-family:"Montserrat",sans-serif;font-weight:900;font-size:62px;letter-spacing:-1px}
  .front__headline .light{display:block;font-family:"Bebas Neue",sans-serif;font-size:80px;line-height:.82}
  .front__badge{position:absolute;left:86px;top:570px;width:236px;height:84px;background:var(--pink);transform:rotate(-3deg);border-radius:6px 14px 4px 18px;
    display:flex;flex-direction:column;align-items:center;justify-content:center;color:var(--white);line-height:1}
  .front__badge span:first-child{font-size:29px}
  .front__badge span:last-child{font-size:28px;transform:rotate(-2deg)}
  .front__dates{position:absolute;left:130px;top:664px;width:148px;height:22px;background:var(--plum);transform:rotate(-1deg);
    font-family:"Bebas Neue",sans-serif;font-size:16px;color:var(--white);text-align:center;line-height:23px}
  .front__stars{position:absolute;left:0;right:0;top:740px;text-align:center}
  .front__presenter{position:absolute;left:0;right:0;top:772px;text-align:center;font-family:"Bebas Neue",sans-serif;font-size:25px;color:var(--white);letter-spacing:.3px}
  .front__blurb{position:absolute;left:36px;right:36px;top:799px;text-align:center;font-family:"Roboto Condensed",sans-serif;font-size:12.5px;color:var(--white);line-height:1.3}

  /* ---------- back ---------- */
  .flyer--back{left:655px;background:var(--paper)}
  .back__food-art{position:absolute;left:0;top:0;width:409px;height:150px;
    background:linear-gradient(180deg,rgba(246,246,244,0) 55%,var(--paper) 100%),linear-gradient(90deg,#6b3a1e 0%,#d9b36a 22%,#d8322a 45%,#e9e4d8 65%,#3d7a2e 100%)}
  .back__learn{position:absolute;left:221px;top:-26px;width:168px;height:168px;border-radius:50%;background:var(--paper);
    display:flex;flex-direction:column;justify-content:center;padding:24px 0 0 24px;color:var(--pink);font-size:34px;font-weight:400;line-height:1;white-space:nowrap}
  .back__learn span:last-child{padding-left:14px}
  .back__topics{position:absolute;left:0;right:46px;top:152px;text-align:right;font-family:"Bebas Neue",sans-serif;color:var(--ink-blue);line-height:1}
  .topic{display:flex;justify-content:flex-end;align-items:flex-end;gap:6px}
  .topic .sm{font-size:30px}
  .topic--intro{font-size:26px;margin-right:24px}
  .topic--intro .sm{font-size:20px}
  .topic--basic{font-size:60px;margin-top:-2px}
  .topic--basic .sm{font-size:40px}
  .topic--gut{font-size:52px;margin-top:-4px}
  .topic--portion{font-size:52px;margin-top:-2px;margin-right:28px}
  .topic--menu{font-size:56px;margin-top:-4px}
  .topic--prep{font-size:78px;margin-top:-6px}
  .topic--eat{font-size:64px;letter-spacing:10px;margin-top:-6px;margin-right:-8px}
  .topic svg{margin-bottom:6px}

  .back__benefits{position:absolute;left:0;top:526px;width:409px;height:232px;background:var(--band-blue);border-radius:50% 50% 0 0/14px 14px 0 0}
  .benefits__title{text-align:center;margin-top:16px;font-family:"Montserrat",sans-serif;font-weight:700;font-size:21px;letter-spacing:5px;color:var(--white)}
  .benefits__row{display:flex;justify-content:center;gap:14px;margin-top:10px}
  .benefit{width:80px;text-align:center;font-family:"Montserrat",sans-serif;font-weight:600;font-size:9.5px;line-height:1.3;color:var(--white)}
  .benefit svg{display:block;margin:0 auto 3px}

  .back__tab{position:absolute;left:0;height:24px;padding:0 14px 0 16px;background:var(--tab-grey);font-family:"Montserrat",sans-serif;font-weight:700;font-size:14px;color:var(--band-blue);line-height:25px}
  .back__tab--prize{top:742px}
  .back__tab--tasting{top:773px}
  .back__reserve{position:absolute;left:277px;top:742px;width:110px;height:32px;background:var(--pink);font-family:"Roboto Condensed",sans-serif;font-weight:700;font-size:24px;color:var(--white);text-align:center;line-height:32px}
  .back__contact{position:absolute;right:22px;top:788px;text-align:right;font-family:"Roboto Condensed",sans-serif;font-size:17px;color:var(--band-blue);line-height:1.1}
  .back__contact strong{font-weight:700}
  .back__supporters{position:absolute;left:12px;top:812px;display:flex;gap:6px;align-items:center}
  .supporter{display:flex;align-items:center;gap:4px;font-family:"Roboto Condensed",sans-serif;font-weight:700;font-size:8px;line-height:1.05;color:var(--plum);width:62px}
  .supporter i{flex:none;width:16px;height:16px;border-radius:50%;background:var(--plum)}
</style>
</head>
<body>
<main class="canvas">

  <!-- Side one -->
  <section class="flyer flyer--front" aria-label="Flyer side one">
    <div class="front__fruit-art" role="img" aria-label="Photo of an orange slice, a red apple and a banana arranged as a smiling fruit face"></div>
    <h1 class="front__headline">
      <span class="heavy">PLATE</span>
      <span class="heavy">BRIGHT</span>
      <span class="light">LIVE</span>
      <span class="light">LIVELY</span>
    </h1>
    <div class="front__badge hand"><span>INTERACTIVE</span><span>WORKSHOPS!</span></div>
    <div class="front__dates">MARCH - APRIL 2019</div>
    <div class="front__stars">
      <svg width="140" height="22" viewBox="0 0 140 22" aria-hidden="true">
        <g fill="var(--star)">
          <polygon id="star" points="11,1 13.8,8 21,8 15.2,12.6 17.4,20 11,15.5 4.6,20 6.8,12.6 1,8 8.2,8"/>
          <use href="#star" x="29"/><use href="#star" x="58"/><use href="#star" x="87"/><use href="#star" x="116"/>
        </g>
      </svg>
    </div>
    <p class="front__presenter">PRESENTED BY QUALIFIED NUTRITIONIST</p>
    <p class="front__blurb">Food for healthier happier life for you and your family (free to central coast residents - all ages welcome</p>
  </section>

  <!-- Side two -->
  <section class="flyer flyer--back" aria-label="Flyer side two">
    <div class="back__food-art" role="img" aria-label="Fresh food flat lay: black beans, pasta, cherry tomatoes, chillies and leafy greens"></div>
    <h2 class="back__learn hand"><span>LEARN</span><span>ABOUT:</span></h2>

    <div class="back__topics">
      <div class="topic topic--intro"><span><span class="sm">FOODS THAT</span> IMPROVE YOUR HEALTH</span></div>
      <div class="topic topic--basic"><span><span class="sm">BASIC</span> NUTRITION</span></div>
      <div class="topic topic--gut"><span>GUT-BRAIN <span class="sm">CONNECTION</span></span></div>
      <div class="topic topic--portion"><span>PORTION <span class="sm">SIZE</span></span>
        <svg width="52" height="46" viewBox="0 0 52 46" aria-hidden="true" fill="none" stroke="var(--ink-blue)" stroke-width="3.5" stroke-linejoin="round">
          <path d="M16 6h26a8 8 0 0 1 3 15v20H19"/><path d="M6 10h26a8 8 0 0 1 3 15v18H9V25a8 8 0 0 1-3-15z"/>
        </svg>
      </div>
      <div class="topic topic--menu">
        <svg width="58" height="52" viewBox="0 0 58 52" aria-hidden="true" fill="none" stroke="var(--ink-blue)" stroke-width="3.5" stroke-linejoin="round">
          <circle cx="29" cy="10" r="7"/><path d="M4 22l25 6 25-6v24l-25 5-25-5z"/><path d="M29 28v23"/>
        </svg>
        <span>MENU <span class="sm">PLANNING</span></span></div>
      <div class="topic topic--prep"><span>PREPARATION</span></div>
      <div class="topic topic--eat">
        <svg width="62" height="62" viewBox="0 0 62 62" aria-hidden="true" fill="none" stroke="var(--ink-blue)" stroke-width="4" stroke-linecap="round">
          <path d="M8 54L44 18"/><ellipse cx="48" cy="13" rx="8" ry="11" transform="rotate(45 48 13)"/>
          <path d="M54 54L20 20"/><path d="M6 8l12 12M12 4l12 12M4 14l12 12"/>
        </svg>
        <span>EATING</span></div>
    </div>

    <div class="back__benefits">
      <h3 class="benefits__title">BENEFITS</h3>
      <div class="benefits__row">
        <div class="benefit"><svg width="34" height="34" viewBox="0 0 34 34" aria-hidden="true"><path fill="var(--white)" d="M12 2h10v10h10v10H22v10H12V22H2V12h10z"/></svg>Improved<br>Health</div>
        <div class="benefit"><svg width="34" height="34" viewBox="0 0 34 34" aria-hidden="true"><path fill="var(--white)" d="M20 1L7 19h9l-3 14 14-19h-9z"/></svg>Improved<br>Energy</div>
        <div class="benefit"><svg width="34" height="34" viewBox="0 0 34 34" aria-hidden="true" fill="none" stroke="var(--white)" stroke-width="2.5"><circle cx="17" cy="17" r="8"/><path d="M17 2v7M17 25v7M2 17h7M25 17h7M6 6l5 5M23 23l5 5M28 6l-5 5M6 28l5-5"/></svg>Manage<br>Chronic Illness</div>
        <div class="benefit"><svg width="34" height="34" viewBox="0 0 34 34" aria-hidden="true" fill="none" stroke="var(--white)" stroke-width="2.5" stroke-linejoin="round"><path d="M4 6l16 0 0 8-16 0z"/><path d="M20 10h6l4 4-12 16"/></svg>Diabetes<br>Type 2</div>
      </div>
      <div class="benefits__row">
        <div class="benefit"><svg width="38" height="40" viewBox="0 0 38 40" aria-hidden="true" fill="none" stroke="var(--white)" stroke-width="2.5"><rect x="4" y="6" width="26" height="30" rx="5"/><circle cx="22" cy="26" r="6"/><path d="M4 14h26"/></svg>Cholesterol</div>
        <div class="benefit"><svg width="38" height="40" viewBox="0 0 38 40" aria-hidden="true" fill="none" stroke="var(--white)" stroke-width="2.5"><circle cx="13" cy="24" r="8"/><path d="M13 16V6h12v22"/><ellipse cx="27" cy="32" rx="5" ry="6"/></svg>Blood<br>Pressure</div>
        <div class="benefit"><svg width="38" height="40" viewBox="0 0 38 40" aria-hidden="true" fill="none" stroke="var(--white)" stroke-width="2.5"><circle cx="12" cy="9" r="5"/><circle cx="26" cy="9" r="5"/><path d="M3 28c0-8 4-12 9-12s9 4 9 12M17 28c0-8 4-12 9-12s9 4 9 12"/><circle cx="19" cy="26" r="4"/><path d="M12 38c0-5 3-8 7-8s7 3 7 8"/></svg>Family<br>Fun</div>
      </div>
    </div>

    <div class="back__tab back__tab--prize">LUCKY DOOR PRIZE</div>
    <div class="back__tab back__tab--tasting">FOOD TASTINGS</div>
    <div class="back__reserve">RESERVE</div>
    <p class="back__contact">for spot online @<br><strong>www.platebright.com.au</strong><br>or call <strong>0462 508 731</strong></p>

    <div class="back__supporters" aria-label="Supported by">
      <span class="supporter"><i></i>Harbourline Shire Council</span>
      <span class="supporter"><i></i>Harbourline Rugby Social Club</span>
      <span class="supporter"><i></i>Pindara Veterans Club</span>
    </div>
  </section>

</main>
</body>
</html>
```